Paws and Meadows is a dog walking service that offers home boarding and pet taxi

I am looking for a eye catching A5 leaflet/flyer design for my dog walking business Paws and Meadows.

The flyer must have my company logo on it (jpeg), a picture of my van (jpeg) and a picture of dogs playing (jpegs 1-5).

The fonts must be easy to read. I am not set on any colour scheme but do like the idea of having a natural background. IE. Green grass and blue sky or some forest setting with green trees. If you don't like this idea or its hard to work with don't worry I am open minded so be creative and do what you thinks best.

I'll provide quick feedback to designs that i like and so we can work together.

The flyers must contain the following:

60 minute group and individual walks
GPS Tracked Walks
Home Boarding
Pet Taxi
Puppy/Pet visits

Offer: 50% off first weeks dogs walks with this flyer.

As well as containing my contact info:

07519306284
www.pawsmeadowsgroup.co.uk
pawsmeadowsgroup@brightmailbox.co.uk

Chatterbook, Quipster and Snapfolio logos must be present as well.

Thanks and Good luck!

Target Market(s)

ANYONE WHO NEEDS THEIR DOG WALKED OR LOOKED AFTER WHEN THEY ARE ON HOLIDAY

Industry/Entity Type

Business

Contact Information for Business Card

THE BUSINESS CARD MUST DISPLAY THE LOGO THAT HAS BEEN UPLOADED IN A FILE. IT MUST LOOK SHARP AND PROFESSIONAL. CONTAIN ALL CONTACT INFO AND HAVE SERVICES OFFERED. SEE PROJECT DESCRIPTION FOR FLYER.

Font styles to use
Serif
Sans Serif

Requirements
Must have
• SEE PROJECT DESCRIPTION
Nice to have
• IT WOULD BE NICE TO HAVE PHOTOS OF MY VAN AND DOGS PLAYING. I HAVE UPLOADED SOME PICS OF VAN TO BE USED AND THERE ARE PICS OF DOGS PLAYING THAT COULD BE USED.

```html
<!DOCTYPE html>
<html lang="en">
<head>
<meta charset="utf-8">
<title>Paws and Meadows – Dog Walking Flyer</title>
<link rel="stylesheet" href="https://fonts.googleapis.com/css2?family=Alegreya:wght@800;900&family=Lora:wght@400;500&display=swap">
<style>
  :root {
    --sky-top: #9fd0e8;
    --sky-mid: #b9dcc8;
    --meadow-light: #8fcf6a;
    --meadow-deep: #3f8f2e;
    --ink: #111411;
    --service-ink: #1d241c;
    --contact-ink: #eef5e4;
    --brand-ink: #1f3a5a;
    --brand-dot: #e0883a;
    --van-sky: #6fb4e6;
    --van-grass: #4c9f34;
  }
  * { margin: 0; padding: 0; box-sizing: border-box; }
  html, body { width: 846px; height: 1200px; overflow: hidden; background: #ffffff; }
  .flyer {
    position: relative;
    width: 846px;
    height: 1200px;
    overflow: hidden;
    font-family: "Lora", Georgia, serif;
  }
  .flyer__backdrop {
    position: absolute;
    inset: 0;
    background:
      radial-gradient(ellipse 60% 40% at 45% 28%, rgba(210,200,150,0.55), rgba(210,200,150,0) 70%),
      linear-gradient(180deg, var(--sky-top) 0%, var(--sky-mid) 30%, #a9d48e 52%, var(--meadow-light) 68%, var(--meadow-deep) 100%);
  }
  .brand {
    position: absolute;
    left: 40px;
    top: 100px;
    display: flex;
    align-items: center;
    gap: 12px;
  }
  .brand__dot {
    width: 34px;
    height: 34px;
    border-radius: 50%;
    background: var(--brand-dot);
  }
  .brand__name {
    font-weight: 500;
    font-size: 26px;
    color: var(--brand-ink);
  }
  .services {
    position: absolute;
    top: 343px;
    left: 0;
    width: 846px;
    list-style: none;
    text-align: center;
  }
  .services__item {
    font-size: 33px;
    line-height: 47.5px;
    letter-spacing: 0.12em;
    white-space: nowrap;
    color: var(--service-ink);
  }
  .offer {
    position: absolute;
    top: 577px;
    left: 0;
    width: 846px;
    text-align: center;
    font-family: "Alegreya", Georgia, serif;
    font-weight: 900;
    font-size: 71px;
    line-height: 97px;
    white-space: nowrap;
    color: var(--ink);
  }
  .van-photo {
    position: absolute;
    left: 408px;
    top: 801px;
    width: 438px;
    height: 399px;
    background: linear-gradient(180deg, var(--van-sky) 0%, #a8d4ef 45%, #7cc35a 62%, var(--van-grass) 100%);
  }
  .contact {
    position: absolute;
    left: 0;
    top: 930px;
    width: 396px;
    text-align: center;
    color: var(--contact-ink);
    font-style: normal;
    font-size: 20px;
    line-height: 33px;
  }
  .contact__heading {
    letter-spacing: 0.04em;
    text-transform: uppercase;
  }
  .contact__email { font-size: 16px; }
  .social {
    position: absolute;
    left: 0;
    top: 1122px;
    width: 396px;
    display: flex;
    justify-content: center;
    gap: 16px;
    list-style: none;
  }
  .social__item {
    display: flex;
    align-items: center;
    gap: 7px;
    font-size: 18px;
    line-height: 24px;
    color: var(--contact-ink);
  }
  .social__square {
    width: 13px;
    height: 13px;
    background: var(--contact-ink);
  }
</style>
</head>
<body>
<main class="flyer">
  <div class="flyer__backdrop" role="img" aria-label="Photo of two dogs carrying a stick together across a sunny grass field under a blue sky"></div>

  <div class="brand">
    <span class="brand__dot"></span>
    <span class="brand__name">Paws and Meadows</span>
  </div>

  <ul class="services">
    <li class="services__item">60 minute group and individual walks</li>
    <li class="services__item">GPS Tracked Walks</li>
    <li class="services__item">Home Boarding</li>
    <li class="services__item">Pet Taxi</li>
    <li class="services__item">Puppy/Pet visits</li>
  </ul>

  <p class="offer">Offer: 50% off first week's<br>dogs walks with this flyer</p>

  <div class="van-photo" role="img" aria-label="Photo of the back of the branded dog walking van, printed with a meadow and sky scene and list of services"></div>

  <address class="contact">
    <p class="contact__heading">Contact details :</p>
    <p>07519306284</p>
    <p>www.pawsmeadowsgroup.co.uk</p>
    <p class="contact__email">pawsmeadowsgroup@brightmailbox.co.uk</p>
  </address>

  <ul class="social">
    <li class="social__item"><span class="social__square"></span>Chatterbook</li>
    <li class="social__item"><span class="social__square"></span>Quipster</li>
    <li class="social__item"><span class="social__square"></span>Snapfolio</li>
  </ul>
</main>
</body>
</html>
```